Consulting Company Business Card

I am looking for a minimalist, classy, professional design on my business card. I would like it to be double-sided. I want to use the font and color scheme of my logo which are attached. Please be creative in the designs that you send me. I want to play off the design of my logo with the inner C that is Green and Blue broken up with the white.
Target Market(s)
Small Businesses
Industry/Entity Type
Consulting
Contact Information for Business Card
Dale M. Whitcombe, CPA CGMA, 555-014-2873, dwhitcombe@vorantaadvisory.example, www.vorantaadvisory.example

```html
<!DOCTYPE html>
<html lang="en">
<head>
<meta charset="utf-8">
<title>Voranta Advisory – Business Card</title>
<link rel="stylesheet" href="https://fonts.googleapis.com/css2?family=Quicksand:wght@500;600;700&display=swap">
<style>
  :root {
    --backdrop: #e4e4e2;
    --card-white: #f9f9f8;
    --card-dark: #1e1b22;
    --card-dark-edge: #2a2630;
    --navy: #2b2d42;
    --teal: #2a8f85;
    --teal-light: #3fb3a6;
    --soft-grey: #d9d9dc;
  }
  * { box-sizing: border-box; margin: 0; padding: 0; }
  html, body {
    width: 1200px; height: 675px; overflow: hidden;
    background: var(--backdrop);
    font-family: "Quicksand", sans-serif;
  }
  .sheet {
    width: 1200px; height: 675px;
    display: flex; align-items: center; justify-content: center; gap: 60px;
  }
  .card {
    position: relative;
    width: 525px; height: 300px;
    border-radius: 16px;
    overflow: hidden;
    box-shadow: 0 10px 26px rgba(0,0,0,.18);
  }

  /* Front */
  .card--front { background: var(--card-white); }
  .card__wash {
    position: absolute; left: -60px; top: -40px; width: 300px; height: 380px;
    background: radial-gradient(ellipse at 40% 50%, rgba(217,217,220,.7), rgba(217,217,220,0) 70%);
  }
  .brand {
    position: absolute; left: 0; right: 0; top: 60px;
    display: flex; align-items: center; justify-content: center; gap: 10px;
  }
  .brand__dot {
    width: 14px; height: 14px; border-radius: 50%; background: var(--teal);
  }
  .brand__name {
    font-weight: 700; font-size: 26px; letter-spacing: 2px;
    color: var(--navy); text-transform: uppercase; white-space: nowrap;
  }
  .rule {
    position: absolute; height: 1.5px; background: var(--teal);
  }
  .rule--top { left: 36px; right: 150px; top: 146px; }
  .rule--bottom { left: 305px; right: 36px; top: 180px; }
  .holder__name {
    position: absolute; right: 36px; top: 156px; white-space: nowrap;
    font-weight: 700; font-size: 15px; letter-spacing: 1px;
    color: var(--navy); text-transform: uppercase;
  }
  .holder__title {
    position: absolute; right: 36px; top: 186px; white-space: nowrap;
    font-weight: 600; font-size: 11px; letter-spacing: 1px; color: var(--teal);
  }
  .contacts {
    position: absolute; left: 36px; top: 160px;
    list-style: none; display: flex; flex-direction: column; gap: 7px;
  }
  .contacts__item {
    display: flex; align-items: center; gap: 9px; white-space: nowrap;
    font-weight: 600; font-size: 12px; line-height: 16px; color: var(--navy);
  }
  .contacts__icon { width: 12px; height: 12px; flex: none; }

  /* Back */
  .card--back { background: var(--card-dark); }
  .card__texture {
    position: absolute; inset: 0;
    background: linear-gradient(120deg, var(--card-dark) 0%, var(--card-dark-edge) 45%, var(--card-dark) 100%);
  }
  .brand--back { top: auto; bottom: 70px; left: 150px; right: 0; }
  .brand--back .brand__name { color: var(--teal-light); font-size: 22px; }
  .brand--back .brand__dot { background: var(--teal-light); }
</style>
</head>
<body>
<main class="sheet">

  <section class="card card--front" aria-label="Business card front">
    <div class="card__wash" role="img" aria-label="Faint oversized brand curve decoration"></div>
    <div class="brand">
      <span class="brand__dot"></span>
      <span class="brand__name">Voranta Advisory</span>
    </div>
    <div class="rule rule--top"></div>
    <p class="holder__name">Dale M. Whitcombe</p>
    <div class="rule rule--bottom"></div>
    <p class="holder__title">CPA CGMA</p>
    <ul class="contacts">
      <li class="contacts__item">
        <svg class="contacts__icon" viewBox="0 0 12 12"><path fill="#2a8f85" d="M2.4 1h2l1 2.6-1.3 1a6 6 0 0 0 3.3 3.3l1-1.3L11 7.6v2a1.2 1.2 0 0 1-1.3 1.2A9.3 9.3 0 0 1 1.2 2.3 1.2 1.2 0 0 1 2.4 1z"/></svg>
        555-014-2873
      </li>
      <li class="contacts__item">
        <svg class="contacts__icon" viewBox="0 0 12 12"><rect x="0.5" y="2" width="11" height="8" rx="1" fill="#2a8f85"/><path d="M1 2.6 6 6.5l5-3.9" stroke="#f9f9f8" stroke-width="1" fill="none"/></svg>
        dwhitcombe@vorantaadvisory.example
      </li>
      <li class="contacts__item">
        <svg class="contacts__icon" viewBox="0 0 12 12"><circle cx="6" cy="6" r="5" fill="none" stroke="#2a8f85" stroke-width="1.2"/><path d="M1 6h10M6 1c-2.5 3-2.5 7 0 10M6 1c2.5 3 2.5 7 0 10" stroke="#2a8f85" stroke-width="0.9" fill="none"/></svg>
        www.vorantaadvisory.example
      </li>
    </ul>
  </section>

  <section class="card card--back" aria-label="Business card back">
    <div class="card__texture" role="img" aria-label="Dark surface with a subtle repeating brand pattern"></div>
    <div class="brand brand--back">
      <span class="brand__dot"></span>
      <span class="brand__name">Voranta Advisory</span>
    </div>
  </section>

</main>
</body>
</html>
```